Need a stunning home page for Car rental company

For a client, I need a slick and sumber home page design. It is a small, local car rental company, with a handful of cars available for rent.
Selling points: affordable lease, availability, always clean cars
The design should be:
- flat and modern
- no, or very few animations/sliders
- CTA: booking form for renting a car.
- 3 featured cars with images and facts (see website) with button to read more about the car.
- fullscreen background video can be an option
- main colour: #efba01
The site is under construction here:
http://tormesbil.ulvenkor.no/
Delivery requirements:
I need a layered & well organised PSD file delivered.

```html
<!DOCTYPE html>
<html lang="no">
<head>
<meta charset="utf-8">
<title>Tormes Bilutleie – Ulvevik</title>
<link href="https://fonts.googleapis.com/css2?family=Open+Sans:wght@400;600;700&display=swap" rel="stylesheet">
<style>
  :root {
    --gold: #efba01;
    --ink: #222222;
    --text: #333333;
    --muted: #b3b3b3;
    --line: #e4e4e4;
    --price-bg: #ececec;
    --footer: #333333;
    --footer-line: #555555;
    --white: #ffffff;
  }
  * { box-sizing: border-box; margin: 0; padding: 0; }
  html, body { width: 968px; height: 1200px; overflow: hidden; }
  body {
    position: relative;
    font-family: "Open Sans", Arial, sans-serif;
    color: var(--text);
    background: var(--white);
  }
  .top-rule { position: absolute; top: 0; left: 0; width: 968px; height: 3px; background: var(--gold); }

  /* Header */
  .site-header { position: absolute; top: 3px; left: 0; width: 968px; height: 97px; background: var(--white); z-index: 2; }
  .utility-bar { position: absolute; top: 13px; left: 616px; display: flex; align-items: center; gap: 6px; font-size: 9px; color: var(--text); }
  .flag { width: 12px; height: 8px; display: block; }
  .utility-bar .ask { margin-left: 10px; }
  .utility-bar .phone { font-size: 13px; font-weight: 600; color: var(--ink); margin-left: 6px; }
  .brand { position: absolute; top: 44px; left: 160px; font-size: 25px; font-weight: 700; letter-spacing: 1px; color: #555555; text-transform: uppercase; }
  .main-nav { position: absolute; top: 47px; left: 479px; display: flex; gap: 16px; font-size: 13px; font-weight: 600; color: var(--ink); }
  .nav-button { position: absolute; top: 43px; left: 713px; width: 96px; height: 26px; border-radius: 6px; background: var(--gold); color: var(--white); font-size: 9.5px; font-weight: 700; display: flex; align-items: center; justify-content: center; }

  /* Hero */
  .hero { position: absolute; top: 100px; left: 0; width: 968px; height: 440px; }
  .hero-photo { position: absolute; inset: 0;
    background: linear-gradient(180deg, #5f8fcc 0%, #8fb4e0 22%, #c6d9ee 40%, #3e5f8c 58%, #7a92b8 72%, #e9eef6 88%, #ffffff 100%); }
  .hero-title { position: absolute; top: 40px; left: 257px; width: 456px; height: 37px; background: rgba(70,70,70,.85); color: var(--white); font-size: 21.5px; font-weight: 700; display: flex; align-items: center; justify-content: center; }
  .hero-text { position: absolute; top: 83px; left: 257px; width: 456px; height: 50px; background: rgba(70,70,70,.72); color: var(--white); font-size: 8px; line-height: 11px; text-align: center; padding: 5px 14px; }

  /* Cars */
  .fleet { position: absolute; top: 371px; left: 159px; display: flex; gap: 16px; z-index: 1; }
  .car-card { width: 205px; height: 373px; background: var(--white); box-shadow: 0 0 4px rgba(0,0,0,.12); padding: 8px 7px 0; }
  .car-photo { width: 191px; height: 132px; display: block; }
  .car-head { display: flex; justify-content: space-between; align-items: center; margin-top: 9px; height: 24px; }
  .car-name { font-size: 12.5px; font-weight: 600; color: var(--ink); }
  .car-price { width: 91px; height: 24px; background: var(--price-bg); color: var(--gold); font-size: 13px; font-weight: 700; display: flex; align-items: center; justify-content: center; }
  .car-specs { list-style: none; border-top: 1px solid var(--line); margin-top: 12px; padding-top: 7px; }
  .car-specs li { display: flex; justify-content: space-between; font-size: 10px; height: 18px; line-height: 18px; color: var(--ink); }
  .reserve { margin-top: 18px; height: 28px; border-radius: 3px; background: var(--gold); color: var(--white); font-size: 12px; font-weight: 700; display: flex; align-items: center; justify-content: center; }

  /* Pitch */
  .pitch { position: absolute; top: 818px; left: 0; width: 968px; text-align: center; font-size: 12.5px; line-height: 19px; font-weight: 700; color: var(--muted); text-transform: uppercase; }
  .call-line { position: absolute; top: 899px; left: 0; width: 968px; text-align: center; font-size: 22px; font-weight: 600; color: var(--ink); }
  .call-line .num { color: var(--gold); }

  /* Footer */
  .site-footer { position: absolute; top: 991px; left: 0; width: 968px; height: 209px; background: var(--footer); color: var(--white); }
  .footer-col { position: absolute; top: 17px; font-size: 8.5px; line-height: 14px; }
  .footer-col h3 { font-size: 12px; font-weight: 700; margin-bottom: 10px; }
  .footer-col ul { list-style: none; }
  .footer-col li { line-height: 18px; padding-left: 6px; }
  .footer-col a { color: var(--white); font-weight: 700; text-decoration: underline; }
  .col-about { left: 159px; width: 200px; }
  .col-cars { left: 380px; }
  .col-contact { left: 601px; line-height: 18px; }
  .footer-rule { position: absolute; top: 136px; left: 159px; width: 650px; height: 1px; background: var(--footer-line); }
  .copyright { position: absolute; top: 156px; left: 159px; font-size: 8.5px; }
  .payments { position: absolute; top: 155px; left: 457px; display: flex; gap: 8px; }
  .payments span { width: 33px; height: 12px; background: #5a5a5a; border-radius: 2px; display: block; }
</style>
</head>
<body>
  <div class="top-rule"></div>

  <header class="site-header">
    <div class="utility-bar">
      <svg class="flag" viewBox="0 0 12 8" aria-label="Norsk"><rect width="12" height="8" fill="#c8102e"/><rect x="3" width="2" height="8" fill="#fff"/><rect y="3" width="12" height="2" fill="#fff"/></svg>
      <svg class="flag" viewBox="0 0 12 8" aria-label="English"><rect width="12" height="8" fill="#1f3a7a"/><rect x="5" width="2" height="8" fill="#fff"/><rect y="3" width="12" height="2" fill="#fff"/><rect x="5.5" width="1" height="8" fill="#c8102e"/><rect y="3.5" width="12" height="1" fill="#c8102e"/></svg>
      <span class="ask">Spørsmål? Ring oss &nbsp;-</span>
      <span class="phone">41526378</span>
    </div>
    <div class="brand">Tormes Bilutleie</div>
    <nav class="main-nav"><span>HJEM</span><span>TJENESTER</span><span>KONTAKT OSS</span></nav>
    <div class="nav-button">BILPARKEN VÅR</div>
  </header>

  <section class="hero">
    <div class="hero-photo" role="img" aria-label="Snow-capped mountains above a fjord under a blue sky"></div>
    <h1 class="hero-title">Velkommen til Tormes Bilutleie – Ulvevik</h1>
    <p class="hero-text">Tormes bilutleie er en bilpark på Ulvevik, og leier ut varebiler og personbiler til deg som trenger en ekstrabil til flytting, ferie, bytur eller hva det måtte være. Vi er uslåelige på service, og mest sannsynlig også på pris. Og du kan stole på at bilen du får fra oss er både ren og pen!</p>
  </section>

  <main class="fleet">
    <article class="car-card">
      <svg class="car-photo" role="img" aria-label="White compact hatchback parked on a street" viewBox="0 0 191 132"><defs><linearGradient id="g1" x1="0" y1="0" x2="0" y2="1"><stop offset="0" stop-color="#6b6a5c"/><stop offset=".5" stop-color="#d9dbdc"/><stop offset="1" stop-color="#8a8a86"/></linearGradient></defs><rect width="191" height="132" fill="url(#g1)"/></svg>
      <div class="car-head"><span class="car-name">Bilmerke</span><span class="car-price">kr 600/døgn</span></div>
      <ul class="car-specs">
        <li><span>Biltype</span><span>Varebil</span></li>
        <li><span>Maks. pers.</span><span>2</span></li>
        <li><span>Ant. dører</span><span>5</span></li>
        <li><span>Min. sjåføralder</span><span>21</span></li>
        <li><span>Girtype</span><span>Manuell</span></li>
        <li><span>Klimaanlegg?</span><span>Ja</span></li>
        <li><span>Ubegrenset km?</span><span>Nei</span></li>
      </ul>
      <div class="reserve">RESERVÉR NÅ</div>
    </article>
    <article class="car-card">
      <svg class="car-photo" role="img" aria-label="Blue hatchback driving on an open road" viewBox="0 0 191 132"><defs><linearGradient id="g2" x1="0" y1="0" x2="0" y2="1"><stop offset="0" stop-color="#8fa6c4"/><stop offset=".55" stop-color="#2f4584"/><stop offset="1" stop-color="#7d7f86"/></linearGradient></defs><rect width="191" height="132" fill="url(#g2)"/></svg>
      <div class="car-head"><span class="car-name">Bilmerke</span><span class="car-price">kr 300/døgn</span></div>
      <ul class="car-specs">
        <li><span>Biltype</span><span>Varebil</span></li>
        <li><span>Maks. pers.</span><span>2</span></li>
        <li><span>Ant. dører</span><span>5</span></li>
        <li><span>Min. sjåføralder</span><span>21</span></li>
        <li><span>Girtype</span><span>Manuell</span></li>
        <li><span>Klimaanlegg?</span><span>Ja</span></li>
        <li><span>Ubegrenset km?</span><span>Nei</span></li>
      </ul>
      <div class="reserve">RESERVÉR NÅ</div>
    </article>
    <article class="car-card">
      <svg class="car-photo" role="img" aria-label="White compact hatchback parked on a street" viewBox="0 0 191 132"><rect width="191" height="132" fill="url(#g1)"/></svg>
      <div class="car-head"><span class="car-name">Bilmerke</span><span class="car-price">kr 900/døgn</span></div>
      <ul class="car-specs">
        <li><span>Biltype</span><span>Varebil</span></li>
        <li><span>Maks. pers.</span><span>2</span></li>
        <li><span>Ant. dører</span><span>5</span></li>
        <li><span>Min. sjåføralder</span><span>21</span></li>
        <li><span>Girtype</span><span>Manuell</span></li>
        <li><span>Klimaanlegg?</span><span>Ja</span></li>
        <li><span>Ubegrenset km?</span><span>Nei</span></li>
      </ul>
      <div class="reserve">RESERVÉR NÅ</div>
    </article>
  </main>

  <p class="pitch">Lorem ipsum dolor sit amet, consectetur adipisicing elit, sed do eiusmod<br>tempor incididunt ut labore et dolore magna aliqua.</p>
  <p class="call-line">Spørsmål? Ring oss &nbsp;- <span class="num">41 526 378</span></p>

  <footer class="site-footer">
    <div class="footer-col col-about">
      <h3>OM OSS</h3>
      <p>Sed ut perspiciatis unde omnis iste natus error sit voluptatem accusantium doloremque laudantium, totam rem aperiam, eaque ipsa quae ab illo.</p>
    </div>
    <div class="footer-col col-cars">
      <h3>ANDRE BILER</h3>
      <ul>
        <li>- Example Tarvo</li>
        <li>- Velmar 34</li>
        <li>- Some car example</li>
        <li>- Hovik 203</li>
      </ul>
    </div>
    <div class="footer-col col-contact">
      <h3>KONTAKT</h3>
      <p>email: <a>email@example.no</a></p>
      <p>telefon: <a>41 526 378</a></p>
    </div>
    <div class="footer-rule"></div>
    <p class="copyright">© Tormes Bilutleie 2014. All rights reserved.</p>
    <div class="payments" aria-label="Accepted payment methods">
      <span></span><span></span><span></span><span></span><span></span><span></span><span></span><span></span>
    </div>
  </footer>
</body>
</html>
```